Business Card Design Project

Need a business card designed for a horse racing/gambling centered company.
Company name is BrightQuill.com.au
Company colours are similar to those in the logo.
Something clean and modern , designer given liberty to be creative.
Incorporate the logo is preferred.
Single or Double Sided fine
Must include :
Name
Mobile Number
Email Address
Reason: Apologies, I have been traveling unexpectedly with business and just need the extra two days to reply and give feedback before making a decision.
Industry/Entity Type
Business

```html
<!DOCTYPE html>
<html lang="en">
<head>
<meta charset="utf-8">
<title>BrightQuill.com.au – Business Card</title>
<link rel="stylesheet" href="https://fonts.googleapis.com/css2?family=Source+Sans+3:wght@400;600&display=swap">
<style>
  :root {
    --paper: #ffffff;
    --ink-blue: #3b3d8f;
    --brand-teal: #138a6c;
    --brand-deep: #0d5c49;
    --band-stripe: #ffffff;
    --band-edge: #e9c93a;
    --photo-top: #b9a89a;
    --photo-bottom: #6e5a4c;
  }
  * { margin: 0; padding: 0; box-sizing: border-box; }
  html, body {
    width: 1200px;
    height: 720px;
    overflow: hidden;
    background: var(--paper);
  }
  .card {
    position: relative;
    width: 1200px;
    height: 720px;
    background: var(--paper);
    font-family: "Source Sans 3", "Myriad Pro", Arial, sans-serif;
    overflow: hidden;
  }
  .race-art {
    position: absolute;
    inset: 0;
    width: 1200px;
    height: 720px;
  }
  .brand {
    position: absolute;
    left: 80px;
    top: 150px;
    display: flex;
    align-items: center;
    gap: 18px;
  }
  .brand-dot {
    width: 80px;
    height: 80px;
    border-radius: 50%;
    background: var(--brand-teal);
    flex: none;
  }
  .brand-name {
    font-size: 40px;
    font-weight: 600;
    color: var(--brand-deep);
    letter-spacing: 0.3px;
  }
  .contact {
    position: absolute;
    right: 80px;
    top: 66px;
    text-align right;
    text-align: right;
    color: var(--ink-blue);
    font-size: 42px;
    font-weight: 400;
    line-height: 1.3;
  }
  .contact .sep { margin: 0 12px; }
</style>
</head>
<body>
  <div class="card">
    <svg class="race-art" viewBox="0 0 1200 720" xmlns="http://www.w3.org/2000/svg">
      <defs>
        <linearGradient id="photoTones" x1="0" y1="0" x2="0" y2="1">
          <stop offset="0" stop-color="var(--photo-top)"/>
          <stop offset="1" stop-color="var(--photo-bottom)"/>
        </linearGradient>
      </defs>
      <g class="finish-band">
        <polygon points="0,470 1200,240 1200,400 0,560" fill="var(--brand-teal)"/>
        <polygon points="0,458 1200,228 1200,240 0,470" fill="var(--band-edge)"/>
        <polygon points="0,540 1200,378 1200,390 0,552" fill="var(--band-stripe)"/>
      </g>
      <rect class="race-photo" role="img"
            aria-label="Photograph of jockeys in coloured silks racing horses toward the finish"
            x="0" y="520" width="1200" height="200" fill="url(#photoTones)"/>
    </svg>

    <div class="brand">
      <span class="brand-dot"></span>
      <span class="brand-name">BrightQuill.com.au</span>
    </div>

    <div class="contact">
      <p class="contact-line">Daniel Marsh<span class="sep">•</span>0400555182</p>
      <p class="contact-line">Daniel@brightquill.com.au</p>
    </div>
  </div>
</body>
</html>
```